Carlin Hobart

I am a songwriter and would like to include a bio, pictures, discography, CD covers and access to some of my music

Target Market(s)

Music Lovers, songwriters publishers

Coding

Coded - Design and coding required

Number of Pages Required

5+ page

Requirements
Must have
• Pictures of my CD covers, pictures of me and either my Music or links to my music
Nice to have
Should not have
• cartoons

```html
<!DOCTYPE html>
<html lang="en">
<head>
<meta charset="utf-8">
<title>Carlin Hobart — Songwriter</title>
<link href="https://fonts.googleapis.com/css2?family=Josefin+Sans:wght@400;600;700&display=swap" rel="stylesheet">
<style>
:root{
  --ink:#000;
  --panel:#0d0b0b;
  --gold:#ffc629;
  --gold-deep:#f5b800;
  --violet:#8e4fb2;
  --white:#fff;
  --muted:#cfcfcf;
  --rule:#3a3a3a;
}
*{box-sizing:border-box;margin:0;padding:0}
html,body{width:1200px;height:3531px;overflow:hidden;background:var(--ink)}
body{font-family:'Josefin Sans',sans-serif;color:var(--white);position:relative}
.abs{position:absolute}
svg.icon{display:block}

/* header */
.site-header{left:0;top:0;width:1200px;height:70px;background:var(--ink);box-shadow:0 4px 10px rgba(0,0,0,.7);z-index:3}
.brand{left:63px;top:18px;font-size:32px;font-weight:700;color:var(--violet);display:flex;align-items:center;gap:8px}
.brand-dot{width:12px;height:12px;background:var(--gold);border-radius:50%}
.main-nav a{position:absolute;top:27px;font-size:16px;color:var(--white);text-decoration:none}
.main-nav a.active{color:var(--gold)}
.search{left:809px;top:17px;width:193px;height:34px;background:var(--white);border-radius:17px}
.search span{position:absolute;left:13px;top:11px;font-size:13px;color:#888}
.search-btn{position:absolute;right:0;top:0;width:34px;height:34px;border-radius:50%;background:var(--gold);display:flex;align-items:center;justify-content:center}
.social-mini{left:1037px;top:26px;display:flex;gap:6px}
.social-mini i{width:20px;height:20px;background:var(--gold);border-radius:3px;display:block}

/* hero */
.hero{left:0;top:70px;width:1200px;height:633px;background:radial-gradient(ellipse at 40% 55%,#f9a21c 0%,#d24d0b 30%,#6a1e05 60%,#1a0a04 100%)}
.hero-photo{left:0;top:0;width:1200px;height:633px;background:linear-gradient(180deg,rgba(0,0,0,.5) 0%,rgba(0,0,0,0) 20%,rgba(0,0,0,0) 65%,rgba(0,0,0,.9) 100%)}
.hero-copy{left:641px;top:140px;width:480px}
.hero-copy h1{font-size:34px;font-weight:600;line-height:42px}
.hero-copy h1 em{font-style:normal;font-weight:700;color:var(--gold);display:block}
.hero-copy p{font-size:14.5px;line-height:19px;margin-top:22px}
.hero-copy p+p{margin-top:18px}
.btn{display:inline-flex;align-items:center;justify-content:center;border-radius:22px;font-size:17px;font-weight:600;font-family:inherit}
.btn-violet{background:var(--violet);border:3px solid var(--gold);color:var(--white)}
.btn-outline{border:3px solid var(--gold);color:var(--white)}
.hero-actions{margin-top:34px;display:flex;gap:20px}
.hero-actions .btn{width:174px;height:43px}

/* player */
.player-bar{left:0;top:703px;width:1200px;height:88px;background:#121010}
.now-pill{left:0;top:0;width:268px;height:88px;background:var(--gold);border-radius:0 44px 44px 0}
.thumb{border-radius:50%;background:radial-gradient(circle at 45% 40%,#e9a23a,#b23a1a 55%,#3a3a3a 100%)}
.now-pill .thumb{position:absolute;left:14px;top:13px;width:62px;height:62px}
.track-title{font-size:17px;line-height:21px;color:#1a1a1a}
.track-title b{font-weight:600;display:block}
.now-pill .track-title{position:absolute;left:106px;top:25px}
.now-pill .track-title span{color:var(--violet)}
.pill-arrow{position:absolute;left:236px;top:36px;width:18px;height:18px;border-radius:50%;background:var(--violet)}
.transport{display:flex;gap:18px;align-items:center}
.progress{position:absolute;height:22px}
.progress .track{position:absolute;left:0;right:0;top:4px;height:3px;background:var(--white)}
.progress .knob{position:absolute;left:-2px;top:0;width:11px;height:11px;border-radius:50%;background:var(--gold)}
.progress .t{position:absolute;top:17px;font-size:12px}
.progress .t.end{right:0}
.vol{position:absolute;width:64px;height:64px;border-radius:50%;border:3px solid var(--gold);display:flex;align-items:center;justify-content:center}
.vol:after{content:"";position:absolute;right:-2px;bottom:0;width:11px;height:11px;border-radius:50%;background:var(--gold)}
.round{position:absolute;width:32px;height:32px;border-radius:50%;border:2px solid var(--white);display:flex;align-items:center;justify-content:center}
.quality-panel{left:932px;top:0;width:268px;height:88px;background:var(--gold);border-radius:44px 0 0 44px}
.quality-btn{position:absolute;left:47px;top:23px;width:176px;height:42px;border:2px solid #fff;border-radius:22px;color:#1a1a1a;font-size:21px;font-weight:600;display:flex;align-items:center;justify-content:center;gap:8px}

/* section headings */
.kicker{width:1200px;text-align:center;font-size:22px}
.section-title{font-size:44px;font-weight:700;color:var(--gold);letter-spacing:1px}

/* events */
.event-card{top:1002px;width:330px;height:403px}
.event-card .frame{position:absolute;left:13px;top:15px;right:13px;bottom:15px;border:2px solid rgba(255,255,255,.9)}
.art-fire{background:linear-gradient(160deg,#5a5046 0%,#c2431a 35%,#f0a23a 55%,#4a4640 100%)}
.art-storm{background:radial-gradient(ellipse at 60% 40%,#7a7fb8 0%,#3a3b78 45%,#141436 100%)}
.art-collage{background:linear-gradient(135deg,#dcd3dc 0%,#c7c6d6 40%,#e6c8d2 70%,#b9b5a0 100%)}
.featured .frame{border:4px solid var(--gold)}
.featured-copy{position:absolute;left:0;right:0;top:38px;text-align:center}
.countdown{font-size:21px;font-weight:700}
.featured-tag{font-size:19px;font-weight:700;color:var(--gold);margin-top:6px}
.featured-name{font-size:45px;font-weight:700;line-height:52px;margin-top:6px}
.featured-copy .btn{width:152px;height:41px;font-size:17px}
.btn-gold{background:var(--gold);color:#1a1a1a}
.btn-ghost{border:3px solid #fff;color:#fff}

/* recently played */
.recent{left:84px;top:1563px;width:1032px;height:416px}
.row{position:absolute;left:0;width:992px;height:104px;border-bottom:1px solid var(--rule)}
.row-num{position:absolute;left:0;top:24px;font-size:58px;font-weight:700;line-height:60px}
.row .thumb{position:absolute;left:91px;top:15px;width:73px;height:73px}
.row .track-title{position:absolute;left:181px;top:31px;color:var(--white)}
.row .track-title b{color:var(--gold)}
.row .transport{position:absolute;left:356px;top:42px}
.row .progress{left:479px;width:324px;top:40px}
.row .vol{left:819px;top:20px}
.row .round.shuffle{left:909px;top:36px}
.row .round.repeat{left:960px;top:36px}
.scroll-track{left:1016px;top:0;width:13px;height:404px;background:#1e1e1e}
.scroll-thumb{left:1016px;top:0;width:13px;height:82px;background:var(--white)}

/* feature */
.feature-photo{left:80px;top:2054px;width:455px;height:456px;background:radial-gradient(ellipse at 55% 50%,#8b7660 0%,#5b4a38 45%,#000 100%)}
.feature-copy{left:584px;top:2122px;width:500px;text-align:center}
.feature-copy h2{font-size:44px;font-weight:700;color:var(--gold);letter-spacing:1px}
.live{display:flex;align-items:center;justify-content:center;gap:12px;font-size:14px;font-weight:700;margin-top:8px}
.live i{width:104px;height:3px;background:var(--gold);display:block}
.feature-lede{font-size:20px;line-height:26px;margin-top:16px}
.feature-body{font-size:14.5px;line-height:19px;margin-top:18px;padding:0 10px}
.feature-copy .btn{width:152px;height:42px;font-size:19px;margin-top:58px}

/* news */
.news-head{left:62px;top:2592px}
.news-sub{left:62px;top:2654px;font-size:14.5px}
.news-rule{left:62px;top:2683px;width:1073px;height:1px;background:var(--rule)}
.news-card{top:2726px;width:337px;height:415px;overflow:hidden}
.news-card .shade{position:absolute;inset:0;background:linear-gradient(180deg,rgba(0,0,0,0) 35%,rgba(0,0,0,.75) 100%)}
.date-badge{position:absolute;left:0;top:0;width:53px;height:54px;background:var(--gold);padding:6px 0 0 8px;line-height:17px}
.date-badge b{font-size:24px;display:block}
.date-badge span{font-size:15px}
.news-card h3{position:absolute;left:13px;top:196px;width:310px;font-size:30px;line-height:34px;font-weight:700;color:var(--gold)}
.news-card p{position:absolute;left:13px;top:305px;width:310px;font-size:14.5px;line-height:19px}
.news-more{position:absolute;right:0;bottom:0;width:44px;height:37px;background:var(--gold);display:flex;align-items:center;justify-content:center}

/* footer */
.foot-photo{left:88px;top:3263px;width:137px;height:180px;border:3px solid #fff;background:linear-gradient(180deg,#8ea3b8 0%,#b4a07a 45%,#e9e6df 100%)}
.foot-about{left:261px;top:3300px;width:290px;font-size:13px;line-height:21px}
.foot-title{font-size:17px;font-weight:600;color:var(--gold)}
.foot-links{left:641px;top:3262px}
.foot-links a{display:block;color:#fff;text-decoration:none;font-size:13.5px;margin-top:17px}
.foot-news{left:828px;top:3262px}
.newsletter{position:absolute;left:0;top:48px;width:285px;height:46px;border:2px solid #fff;background:#fff}
.newsletter span{position:absolute;left:13px;top:16px;font-size:13px;color:#777}
.newsletter .send{position:absolute;right:0;top:0;width:46px;height:42px;background:#000;display:flex;align-items:center;justify-content:center}
.foot-social{position:absolute;left:0;top:116px;display:flex;gap:15px}
.foot-social i{display:block;width:30px;height:30px;background:var(--gold);border-radius:3px}
.foot-rule{left:66px;top:3478px;width:1068px;height:1px;background:var(--rule)}
.copyright{left:0;top:3497px;width:1200px;text-align:center;font-size:17px;color:var(--gold)}
</style>
</head>
<body>
<svg width="0" height="0" style="position:absolute">
  <defs>
    <symbol id="i-prev" viewBox="0 0 20 16"><rect x="0" y="1" width="3" height="14" fill="currentColor"/><path d="M11 8 3 1v14zM19 1l-8 7 8 7z" fill="currentColor"/></symbol>
    <symbol id="i-play" viewBox="0 0 14 16"><path d="M1 0l13 8-13 8z" fill="currentColor"/></symbol>
    <symbol id="i-next" viewBox="0 0 20 16"><rect x="17" y="1" width="3" height="14" fill="currentColor"/><path d="M9 8l8-7v14zM1 1l8 7-8 7z" fill="currentColor"/></symbol>
    <symbol id="i-vol" viewBox="0 0 24 20"><path d="M1 7h5l6-5v16l-6-5H1z" fill="currentColor"/><path d="M15 6q3 4 0 8M18 3q6 7 0 14" stroke="currentColor" stroke-width="2" fill="none"/></symbol>
    <symbol id="i-shuffle" viewBox="0 0 16 14"><path d="M1 3h3l7 8h3M1 11h3l7-8h3" stroke="currentColor" stroke-width="1.8" fill="none"/><path d="M13 0l3 3-3 3zM13 8l3 3-3 3z" fill="currentColor"/></symbol>
    <symbol id="i-repeat" viewBox="0 0 16 16"><path d="M13 6A5.5 5.5 0 0 0 3 5M3 10a5.5 5.5 0 0 0 10 1" stroke="currentColor" stroke-width="1.8" fill="none"/><path d="M10 6h5V1zM6 10H1v5z" fill="currentColor"/></symbol>
    <symbol id="i-chev" viewBox="0 0 14 10"><path d="M1 8l6-6 6 6" stroke="currentColor" stroke-width="2.6" fill="none"/></symbol>
    <symbol id="i-go" viewBox="0 0 24 24"><circle cx="12" cy="12" r="10" stroke="currentColor" stroke-width="2.4" fill="none"/><path d="M10 7l5 5-5 5" stroke="currentColor" stroke-width="2.4" fill="none"/></symbol>
  </defs>
</svg>

<header class="site-header abs">
  <div class="brand abs"><i class="brand-dot"></i>Sonora</div>
  <nav class="main-nav">
    <a class="active" style="left:237px">Home</a>
    <a style="left:354px">About Us</a>
    <a style="left:497px">Event</a>
    <a style="left:613px">Blog</a>
    <a style="left:721px">Contact</a>
  </nav>
  <div class="search abs"><span>Search Music Here..</span>
    <div class="search-btn"><svg class="icon" width="16" height="16" viewBox="0 0 16 16"><circle cx="6.5" cy="6.5" r="4.8" stroke="#fff" stroke-width="2.2" fill="none"/><path d="M10 10l5 5" stroke="#fff" stroke-width="2.4"/></svg></div>
  </div>
  <div class="social-mini abs"><i></i><i></i><i></i><i></i></div>
</header>

<section class="hero abs">
  <div class="hero-photo abs" role="img" aria-label="Photo of Carlin Hobart standing before a glowing fire crater at night"></div>
  <div class="hero-copy abs">
    <h1>This Month’s <em>Record Breaking Albums !</em></h1>
    <p>Dream your moments, Until I Met You, Gimme Some Courage, Dark Alley, One More Of A Stranger, Endless</p>
    <p>Things, The Heartbeat Stops, Walking Promises, Desired Games and many more...</p>
    <div class="hero-actions"><span class="btn btn-violet">Listen Now</span><span class="btn btn-outline">Download Now</span></div>
  </div>
</section>

<section class="player-bar abs">
  <div class="now-pill abs">
    <div class="thumb" role="img" aria-label="Album cover thumbnail"></div>
    <div class="track-title"><b>Until I Met You</b><span>Mira Fenwick</span></div>
    <i class="pill-arrow"></i>
  </div>
  <div class="transport abs" style="left:281px;top:36px;color:#fff">
    <svg class="icon" width="20" height="16"><use href="#i-prev"/></svg>
    <svg class="icon" width="14" height="16"><use href="#i-play"/></svg>
    <svg class="icon" width="20" height="16"><use href="#i-next"/></svg>
  </div>
  <div class="progress" style="left:402px;top:28px;width:324px"><i class="track"></i><i class="knob"></i><span class="t">00:00</span><span class="t end">04:27</span></div>
  <div class="vol" style="left:743px;top:12px;color:#fff"><svg class="icon" width="24" height="20"><use href="#i-vol"/></svg></div>
  <div class="round" style="left:832px;top:28px;color:#fff"><svg class="icon" width="15" height="13"><use href="#i-shuffle"/></svg></div>
  <div class="round" style="left:884px;top:28px;color:#fff"><svg class="icon" width="15" height="15"><use href="#i-repeat"/></svg></div>
  <div class="quality-panel abs"><div class="quality-btn">Quality <svg class="icon" width="16" height="11" style="color:#1a1a1a"><use href="#i-chev"/></svg></div></div>
</section>

<p class="kicker abs" style="top:876px">Get Read For The Summer 2020</p>
<h2 class="section-title abs" style="left:0;width:1200px;text-align:center;top:906px">UPCOMING EVENTS</h2>

<article class="event-card abs art-fire" style="left:87px" role="img" aria-label="Album cover: a burning record sleeve on a café table"><i class="frame"></i></article>
<article class="event-card featured abs art-storm" style="left:436px">
  <div class="abs" style="inset:0" role="img" aria-label="Stormy sky with lightning and a silhouetted singer"></div>
  <i class="frame"></i>
  <div class="featured-copy">
    <div class="countdown">03D 16H 20M 10S</div>
    <div class="featured-tag">FEATURED</div>
    <div class="featured-name">BEACH<br>PARTY<br>MUSIC</div>
    <div style="margin-top:12px"><span class="btn btn-gold">Buy Ticket</span></div>
    <div style="margin-top:16px"><span class="btn btn-ghost">View Details</span></div>
  </div>
</article>
<article class="event-card abs art-collage" style="left:784px" role="img" aria-label="Album cover: pastel collage with a childhood photo, titled by Carlin Hobart"><i class="frame"></i></article>

<h2 class="section-title abs" style="left:84px;top:1488px;color:var(--gold)">Recently Played</h2>

<section class="recent abs">
  <div class="row" style="top:0">
    <span class="row-num" style="color:var(--gold)">01</span>
    <div class="thumb" role="img" aria-label="Album cover thumbnail"></div>
    <div class="track-title"><b>Until I Met You</b>Mira Fenwick</div>
    <div class="transport"><svg class="icon" width="20" height="16"><use href="#i-prev"/></svg><svg class="icon" width="14" height="16"><use href="#i-play"/></svg><svg class="icon" width="20" height="16"><use href="#i-next"/></svg></div>
    <div class="progress"><i class="track"></i><i class="knob"></i><span class="t">00:00</span><span class="t end">04:27</span></div>
    <div class="vol"><svg class="icon" width="24" height="20"><use href="#i-vol"/></svg></div>
    <div class="round shuffle"><svg class="icon" width="15" height="13"><use href="#i-shuffle"/></svg></div>
    <div class="round repeat"><svg class="icon" width="15" height="15"><use href="#i-repeat"/></svg></div>
  </div>
  <div class="row" style="top:104px">
    <span class="row-num">02</span>
    <div class="thumb" role="img" aria-label="Album cover thumbnail"></div>
    <div class="track-title"><b>Until I Met You</b>Mira Fenwick</div>
    <div class="transport"><svg class="icon" width="20" height="16"><use href="#i-prev"/></svg><svg class="icon" width="14" height="16"><use href="#i-play"/></svg><svg class="icon" width="20" height="16"><use href="#i-next"/></svg></div>
    <div class="progress"><i class="track"></i><i class="knob"></i><span class="t">00:00</span><span class="t end">04:27</span></div>
    <div class="vol"><svg class="icon" width="24" height="20"><use href="#i-vol"/></svg></div>
    <div class="round shuffle"><svg class="icon" width="15" height="13"><use href="#i-shuffle"/></svg></div>
    <div class="round repeat"><svg class="icon" width="15" height="15"><use href="#i-repeat"/></svg></div>
  </div>
  <div class="row" style="top:208px">
    <span class="row-num">03</span>
    <div class="thumb" role="img" aria-label="Album cover thumbnail"></div>
    <div class="track-title"><b>Until I Met You</b>Mira Fenwick</div>
    <div class="transport"><svg class="icon" width="20" height="16"><use href="#i-prev"/></svg><svg class="icon" width="14" height="16"><use href="#i-play"/></svg><svg class="icon" width="20" height="16"><use href="#i-next"/></svg></div>
    <div class="progress"><i class="track"></i><i class="knob"></i><span class="t">00:00</span><span class="t end">04:27</span></div>
    <div class="vol"><svg class="icon" width="24" height="20"><use href="#i-vol"/></svg></div>
    <div class="round shuffle"><svg class="icon" width="15" height="13"><use href="#i-shuffle"/></svg></div>
    <div class="round repeat"><svg class="icon" width="15" height="15"><use href="#i-repeat"/></svg></div>
  </div>
  <div class="row" style="top:312px">
    <span class="row-num">04</span>
    <div class="thumb" role="img" aria-label="Album cover thumbnail"></div>
    <div class="track-title"><b>Until I Met You</b>Mira Fenwick</div>
    <div class="transport"><svg class="icon" width="20" height="16"><use href="#i-prev"/></svg><svg class="icon" width="14" height="16"><use href="#i-play"/></svg><svg class="icon" width="20" height="16"><use href="#i-next"/></svg></div>
    <div class="progress"><i class="track"></i><i class="knob"></i><span class="t">00:00</span><span class="t end">04:27</span></div>
    <div class="vol"><svg class="icon" width="24" height="20"><use href="#i-vol"/></svg></div>
    <div class="round shuffle"><svg class="icon" width="15" height="13"><use href="#i-shuffle"/></svg></div>
    <div class="round repeat"><svg class="icon" width="15" height="15"><use href="#i-repeat"/></svg></div>
  </div>
  <i class="scroll-track abs"></i><i class="scroll-thumb abs"></i>
</section>

<div class="feature-photo abs" role="img" aria-label="Portrait of Carlin Hobart in a white shirt against a stone wall"></div>
<section class="feature-copy abs">
  <h2>EMBER LANE</h2>
  <div class="live"><i></i>LIVE<i></i></div>
  <p class="feature-lede">Lorem Ipsum is simply dummy text of the printing and typesetting industry.</p>
  <p class="feature-body">Lorem ipsum dolor sit amet, consectetur adipisicing elit. Rerum atque tempore iste. Lorem ipsum dolor sit amet, consectetur adipisicing elit. Rerum atque tempore iste. Lorem ipsum dolor sit amet, consectetur adipisicing elit. Rerum atque tempore iste.</p>
  <span class="btn btn-violet">Buy Tickets</span>
</section>

<h2 class="section-title abs news-head">LATEST NEWS</h2>
<p class="news-sub abs">Here is the movies list of 2020 of our production, enjoy the movie and stay with us.</p>
<i class="news-rule abs"></i>

<article class="news-card abs art-storm" style="left:82px">
  <div class="abs" style="inset:0" role="img" aria-label="Stormy sky with lightning and music notes"></div><i class="shade"></i>
  <div class="date-badge"><b>05</b><span>Feb</span></div>
  <h3>Nam Lectus Nibh Consequat Aucibus Turpis.</h3>
  <p>Lorem ipsum dolor sit amet, consectetur adipisicing elit, sed do eiusmod tempor incididunt ut labore et dolore magna aliqua.Lorem ipsum dolor sit amet,</p>
  <span class="news-more"><svg class="icon" width="24" height="24" style="color:#fff"><use href="#i-go"/></svg></span>
</article>
<article class="news-card abs art-collage" style="left:432px">
  <div class="abs" style="inset:0" role="img" aria-label="Album back cover with track credits and a colourful bird"></div><i class="shade"></i>
  <div class="date-badge"><b>14</b><span>Feb</span></div>
  <h3>Nam Lectus Nibh Consequat Aucibus Turpis.</h3>
  <p>Lorem ipsum dolor sit amet, consectetur adipisicing elit, sed do eiusmod tempor incididunt ut labore et dolore magna aliqua.Lorem ipsum dolor sit amet,</p>
  <span class="news-more"><svg class="icon" width="24" height="24" style="color:#fff"><use href="#i-go"/></svg></span>
</article>
<article class="news-card abs art-collage" style="left:781px">
  <div class="abs" style="inset:0" role="img" aria-label="Album cover: pastel collage titled by Carlin Hobart"></div><i class="shade"></i>
  <div class="date-badge"><b>21</b><span>Feb</span></div>
  <h3>Nam Lectus Nibh Consequat Aucibus Turpis.</h3>
  <p>Lorem ipsum dolor sit amet, consectetur adipisicing elit, sed do eiusmod tempor incididunt ut labore et dolore magna aliqua.Lorem ipsum dolor sit amet,</p>
  <span class="news-more"><svg class="icon" width="24" height="24" style="color:#fff"><use href="#i-go"/></svg></span>
</article>

<footer>
  <div class="foot-photo abs" role="img" aria-label="Photo of Carlin Hobart in a hat outdoors"></div>
  <p class="foot-about abs">Mauris malesuada arcu eu posuere eleifen. Ut egestas tortor at leo egestas tincidunt. Nam tincidunt metus tristique tristique viverra. Mauris erat ante, egestas vitae dapibus sed.</p>
  <div class="foot-links abs">
    <div class="foot-title">Links</div>
    <a>Home</a><a>About Us</a><a>Event</a><a>Blog</a><a>Contact</a>
  </div>
  <div class="foot-news abs">
    <div class="foot-title">Newsletter</div>
    <div class="newsletter"><span>Enter Email</span>
      <div class="send"><svg class="icon" width="20" height="20" viewBox="0 0 20 20"><path d="M1 9 19 1 12 19 9 11z" fill="var(--gold)"/></svg></div>
    </div>
    <div class="foot-social"><i></i><i></i><i></i><i></i></div>
  </div>
  <i class="foot-rule abs"></i>
  <p class="copyright abs">CopyRight© 2020 Company Name . All Rights Reserved.</p>
</footer>
</body>
</html>
```